Two (Similar) Posters - Both 11" x 17"

We are looking for two posters - both 11" x 17" (vertical orientation) - to promote two consecutive, cardiology-related events:

Poster #1) The Inaugural New York RMC Quizline Competition, Cocktail Reception and Whiskey Tasting (http://brelvan-hsq.org/quizline-and-reception)

and

Poster #2) The 89th Annual Scientific Session and 27th Annual Meeting (http://brelvan-hsq.org/2017annualmtg)

#1 is a cocktail party with a whiskey tasting that will also feature a gameshow-like event with the med students, and #2 is an educational conference for doctors

Target Market(s)

Healthcare providers (Please do not include stock images of medical professionals; in fact, please use caution with any stock imagery, as it most likely will not be appropriate.)

Industry/Entity Type

Education

Colors

Designer to choose colors to be used in the design.

Requirements
Must have
• Each poster design should include:
• - the 4 logos of the participating organizations (I can upload various other versions if needed) along with the "wording" that goes alongside each one (see "STD_small" image as an example)
• - name of event
• - date, time and location
• - where to register
• - where to get more information
• - some artistic flavor or detailing
• Final (raw) files in an .ai, .psd, .eps or .idml format are required upon project completion.
Nice to have
• It's not crucial that these two posters "match," but it would be nice if they at least coordinated with each other. Would be nice if the designer could stay close to our color scheme (can be found here - http://brelvan-hsq.org/), but this isn't crucial. Posters should be upscale, neat and professional.
Should not have
• Should not be too difficult to read. These are posters that will likely be hanging on a bulletin board in hospital staff break rooms. Should not be too cartoon-like or silly. The two should not look EXACTLY the same in case people think that they are the same poster.

```html
<!DOCTYPE html>
<html lang="en">
<head>
<meta charset="utf-8">
<title>Event Posters</title>
<link href="https://fonts.googleapis.com/css2?family=Cinzel:wght@400;500&family=Tinos:wght@400;700&display=swap" rel="stylesheet">
<style>
  :root {
    --navy: #1f3b67;
    --navy-deep: #19325a;
    --gold: #d2ac68;
    --gold-soft: #e3c58e;
    --ink: #1b1b1b;
    --paper: #ffffff;
    --band: #ececec;
    --stage: #d9d9d9;
  }
  * { box-sizing: border-box; margin: 0; padding: 0; }
  html, body { width: 1200px; height: 831px; overflow: hidden; }
  body { background: var(--stage); position: relative; font-family: "Tinos", "Times New Roman", serif; }

  .poster {
    position: absolute; top: 61px; width: 466px; height: 710px;
    background: var(--navy); box-shadow: 0 6px 14px rgba(0,0,0,.35);
  }
  .poster--quiz { left: 60px; }
  .poster--session { left: 673px; }

  .photo-strip { position: absolute; left: 0; width: 100%; height: 55px; }
  .photo-strip--top { top: 0; }
  .photo-strip--bottom { bottom: 0; background: linear-gradient(90deg, #5a3d22 0%, #8a5a2e 18%, #3b2a1e 32%, #2b2f6e 50%, #6b6fc0 58%, #3a2b22 70%, #a8733b 86%, #6a4a2a 100%); }
  .poster--quiz .photo-strip--top { background: linear-gradient(90deg, #3d4fa8 0%, #7a8de0 14%, #2a2f6a 30%, #8a3a5a 50%, #4a3a2e 70%, #c99a6a 80%, #2a2a3a 100%); }
  .poster--session .photo-strip--top { background: linear-gradient(90deg, #6a5a3a 0%, #c9b07a 14%, #3a3f8a 40%, #5a6ad0 55%, #4a3524 72%, #c08a4a 86%, #7a5430 100%); }

  .frame {
    position: absolute; left: 18px; top: 78px; width: 430px; height: 554px;
    background: var(--paper); border: 6px solid var(--gold);
  }
  .frame::after {
    content: ""; position: absolute; inset: 4px; border: 1.5px solid var(--gold); pointer-events: none;
  }

  .c { position: absolute; left: 0; right: 0; text-align: center; transform: translateY(-50%); white-space: nowrap; }
  .title { font-family: "Cinzel", serif; color: var(--navy); font-weight: 500; letter-spacing: .3px; }
  .subtitle { font-family: "Cinzel", serif; color: var(--ink); font-size: 11.5px; }
  .date { font-weight: 700; color: var(--navy); font-size: 22px; }
  .when, .address { font-weight: 700; color: var(--ink); font-size: 11.5px; }
  .venue { font-weight: 700; color: var(--navy); font-size: 22px; }
  .register-head { font-family: "Cinzel", serif; color: var(--ink); font-size: 14.5px; letter-spacing: .5px; }
  .register-url { font-weight: 700; color: var(--navy); font-size: 13.5px; }
  .info-line { font-weight: 700; color: var(--ink); font-size: 10px; }
  .contact { font-weight: 700; color: var(--ink); font-size: 10.5px; display: flex; justify-content: center; align-items: center; gap: 6px; }
  .contact .or { margin: 0 22px; }
  .contact svg { width: 10px; height: 10px; }

  .ornament {
    position: absolute; left: 76px; width: 314px; height: 22px; transform: translateY(-50%);
    background: linear-gradient(90deg, rgba(210,172,104,0) 0%, var(--gold) 12%, var(--gold-soft) 50%, var(--gold) 88%, rgba(210,172,104,0) 100%);
    border-radius: 11px; opacity: .85;
  }

  .price { position: absolute; top: 328px; width: 161px; height: 78px; text-align: center; }
  .price::after { content: ""; position: absolute; inset: 6px; border: 2px solid var(--paper); }
  .price--member { left: 46px; background: var(--gold); color: var(--navy); }
  .price--guest { left: 254px; background: var(--navy); color: var(--gold); }
  .price-amount { font-family: "Cinzel", serif; font-size: 25px; padding-top: 18px; line-height: 1; }
  .price-note { font-size: 7.5px; font-weight: 700; margin-top: 4px; }

  .about {
    position: absolute; left: 38px; top: 462px; width: 392px; height: 85px;
    background: var(--navy-deep); padding: 13px 16px; color: var(--paper);
    font-size: 7.6px; line-height: 1.45; text-align: justify;
  }
  .about::after { content: ""; position: absolute; inset: 4px; border: 1.5px solid var(--paper); }

  .partners {
    position: absolute; left: 30px; top: 565px; width: 406px; height: 54px; background: var(--band);
    display: flex; align-items: center; justify-content: space-between; padding: 0 4px;
  }
  .partner { display: flex; align-items: center; gap: 5px; }
  .partner-mark { width: 34px; height: 34px; border-radius: 50%; background: var(--paper); border: 2px solid var(--navy); flex: none; }
  .partner-name { font-size: 5.6px; color: var(--navy); line-height: 1.2; width: 68px; }
</style>
</head>
<body>

<section class="poster poster--quiz">
  <div class="photo-strip photo-strip--top" role="img" aria-label="Photo of a lively reception with stage lights"></div>
  <div class="frame"></div>

  <div class="c title" style="top:114px;font-size:21px;">The Inaugural New York</div>
  <div class="c title" style="top:136px;font-size:16.5px;">RMC Quizline Competition</div>
  <div class="c subtitle" style="top:160px;">Cocktail Reception &amp; Whiskey Tasting</div>
  <div class="ornament" style="top:189px;" role="img" aria-label="Gold scroll ornament divider"></div>

  <div class="c date" style="top:226px;">December 6th, 2017</div>
  <div class="c when" style="top:248px;">Wednesday, from 6:30 p.m. to 10:30 p.m.</div>
  <div class="c venue" style="top:277px;">Oak &amp; Ember</div>
  <div class="c address" style="top:299px;">14 E 41st St, New York, NY 10017</div>

  <div class="price price--member">
    <div class="price-amount">FREE</div>
    <div class="price-note">for BHSQ/RMC Members</div>
  </div>
  <div class="price price--guest">
    <div class="price-amount">$30</div>
    <div class="price-note">for nonmembers and guests</div>
  </div>

  <div class="ornament" style="top:442px;" role="img" aria-label="Gold scroll ornament divider"></div>

  <div class="c register-head" style="top:480px;">Register Online</div>
  <div class="c register-url" style="top:498px;">brelvan-hsq.org/quizline-and-reception</div>
  <div class="c info-line" style="top:522px;">For more information or to inquire about becoming an exhibitor</div>
  <div class="c contact" style="top:539px;">
    <svg viewBox="0 0 10 10" aria-hidden="true"><circle cx="5" cy="5" r="5" fill="#1f3b67"/><path d="M3 2.4c.4-.3.8 0 1 .5l.3.7-.5.5c.3.7.8 1.2 1.5 1.5l.5-.5.7.3c.5.2.8.6.5 1-.6.8-1.6.6-2.5 0C3.6 5.7 3 5 2.6 4.2c-.4-.8-.2-1.4.4-1.8z" fill="#fff"/></svg>
    <span>(212) 555-0148</span><span class="or">or</span>
    <svg viewBox="0 0 10 10" aria-hidden="true"><circle cx="5" cy="5" r="5" fill="#1f3b67"/><rect x="2.5" y="3.3" width="5" height="3.4" fill="#fff"/><path d="M2.5 3.3L5 5.3l2.5-2" stroke="#1f3b67" stroke-width=".6" fill="none"/></svg>
    <span>ask@brelvan-hsq.org</span>
  </div>

  <div class="partners">
    <div class="partner"><span class="partner-mark"></span><span class="partner-name">Presented by<br>The Brelvan Heart<br>Society, Inc</span></div>
    <div class="partner"><span class="partner-mark"></span><span class="partner-name">of the<br>The Brelvan State Chapter<br>Regional Medical Council</span></div>
    <div class="partner"><span class="partner-mark"></span><span class="partner-name">In Association With<br>Brelvan Cardiac Center</span></div>
    <div class="partner"><span class="partner-mark"></span></div>
  </div>

  <div class="photo-strip photo-strip--bottom" role="img" aria-label="Row of venue interior photos: lounge, bar and ballroom"></div>
</section>

<section class="poster poster--session">
  <div class="photo-strip photo-strip--top" role="img" aria-label="Row of venue interior photos: lounge and lit ballroom stage"></div>
  <div class="frame"></div>

  <div class="c title" style="top:115px;font-size:18px;">The 89th Annual Scientific Session &amp;</div>
  <div class="c title" style="top:135px;font-size:15px;">27th Annual Meeting</div>
  <div class="ornament" style="top:178px;" role="img" aria-label="Gold scroll ornament divider"></div>

  <div class="c date" style="top:222px;">December 7th, 2017</div>
  <div class="c when" style="top:243px;">Thursday, from 7:30 a.m. to 3 p.m.</div>
  <div class="c venue" style="top:274px;">The Halvorsen Ballroom</div>
  <div class="c address" style="top:294px;">22 E. 29th St., New York, NY</div>

  <div class="ornament" style="top:334px;" role="img" aria-label="Gold scroll ornament divider"></div>

  <div class="c register-head" style="top:372px;">Register Online</div>
  <div class="c register-url" style="top:391px;">brelvan-hsq.org/2017annualmtg</div>
  <div class="c info-line" style="top:418px;">For more information or to inquire about becoming an exhibitor</div>
  <div class="c contact" style="top:435px;">
    <svg viewBox="0 0 10 10" aria-hidden="true"><circle cx="5" cy="5" r="5" fill="#1f3b67"/><path d="M3 2.4c.4-.3.8 0 1 .5l.3.7-.5.5c.3.7.8 1.2 1.5 1.5l.5-.5.7.3c.5.2.8.6.5 1-.6.8-1.6.6-2.5 0C3.6 5.7 3 5 2.6 4.2c-.4-.8-.2-1.4.4-1.8z" fill="#fff"/></svg>
    <span>(212) 555-0148</span><span class="or">or</span>
    <svg viewBox="0 0 10 10" aria-hidden="true"><circle cx="5" cy="5" r="5" fill="#1f3b67"/><rect x="2.5" y="3.3" width="5" height="3.4" fill="#fff"/><path d="M2.5 3.3L5 5.3l2.5-2" stroke="#1f3b67" stroke-width=".6" fill="none"/></svg>
    <span>ask@brelvan-hsq.org</span>
  </div>

  <div class="about">The Annual Scientific Session brings together cardiologists, cardio-thoracic surgeons, internists, family practitioners, gerontologists, oncologists, cardiac nurse practitioners, physician assistants, cardiology fellows in training (FITs) and all members of the cardiac care team, and, this year, will feature the winners of the Annual Young Investigators' Competition for case studies and abstracts (posters), which is now open!</div>

  <div class="partners">
    <div class="partner"><span class="partner-mark"></span><span class="partner-name">Presented by<br>The Brelvan Heart<br>Society, Inc</span></div>
    <div class="partner"><span class="partner-mark"></span><span class="partner-name">of the<br>The Brelvan State Chapter<br>Regional Medical Council</span></div>
    <div class="partner"><span class="partner-mark"></span><span class="partner-name">In Association With<br>Brelvan Cardiac Center</span></div>
    <div class="partner"><span class="partner-mark"></span></div>
  </div>

  <div class="photo-strip photo-strip--bottom" role="img" aria-label="Row of venue interior photos: lounge, bar and ballroom"></div>
</section>

</body>
</html>
```